Food fans website needs a desktop homepage design

We need a desktop homepage design for Zestmora.co.uk, a website to help you to find the best restaurants in each main city of Europe, with initial focus on London. It is not a directory with thousands of restaurants and reviews, else lists of top 20 restaurants for each area of the city. Food fans from all around the city will be able to keep an itinerary of where they eat, showing them later funny stats like "this month you really went for pizzas, don't you?". Keep it funny but professional.

A bit of branding has been done but this project give you total freedom to design the homepage of the site. The design must be a mix between minimal, flat and clean layout. The main idea is to keep it simple, easy to use and showing just the necessary elements.

For the font and colour scheme, we would like to use a thin but energetic font using the #E1393A colour as starting point even if you have freedom to slightly modify it. Blacks, greys and whites can be the secondary colours but we are open to introduce another main colour to the site like green, orange or yellow.

A simple wireframe has been attached to help you but the main elements that the page requires are the next:
- Panoramic fancy image in the header to contain the logo and the search form (the fields of the form are specified on the wireframe) and maybe some animated text to fill the right gap.
- List of results (10 results per page) showing the main info for each restaurant: name, thumbnail, location (zone, area), category, price, description, rating (no with stars please) and whatever you want to add that makes sense.
- Right hand sidebar with 3 widgets: Categories, Location and prices.

You can get the icons from vendrako.net.

We are open to have some text-shadows, rounded corners, box-shadows but trying to keep it minimal, flat and clean as much as possible. The main attractive of the site are the food/restaurant images.

Target Market(s)

22 - 45 food fans lovers from the city. busy people that want to disconnect and relax through the food. The don't mind to pay for quality and new experiences. Up to meet new places around them.

Industry/Entity Type

Restaurant

Requirements
Must have
• Panoramic image in the header, restaurants search form as per wireframe, list results with pagination, right hand sidebar with the widgets mention above and a nice footer with extra elements like "latest restaurants, latest tweets, etc.."
Nice to have
• This site will only be supported by the latest browsers so the idea is to have nice CSS3 transitions all around. Have that in mind at the time to design it even if you cannot show it on the design.
Should not have
• Busy backgrounds and unnecessary images that would slow down the page load.

```html
<!DOCTYPE html>
<html lang="en">
<head>
<meta charset="utf-8">
<title>Zestmora In London – Best Restaurants Near You</title>
<link rel="stylesheet" href="https://fonts.googleapis.com/css2?family=Open+Sans:ital,wght@0,300;0,400;0,600;0,700;1,700&display=swap">
<style>
:root{
  --red:#e1393a;
  --red-dark:#c92b2c;
  --green:#4cae3c;
  --ink:#2a2a2a;
  --text:#3c3c3c;
  --line:#e3e3e3;
  --page:#f3eeee;
  --panel:#ffffff;
  --alt:#f6f5f5;
  --footer:#1c1c1c;
  --footer-box:#2b2b2b;
  --footer-text:#cfcfcf;
  --blue:#2d8fd6;
  --hero-top:#8a4a30;
  --hero-bottom:#d8d49a;
  --thumb:#8c5424;
}
*{box-sizing:border-box;margin:0;padding:0}
html,body{width:713px;height:1200px;overflow:hidden}
body{font-family:"Open Sans",Arial,sans-serif;color:var(--text);background:var(--page)}
.page{position:relative;width:713px;height:1200px;overflow:hidden;background:var(--page)}
.abs{position:absolute}

/* top bar */
.topbar{left:0;top:0;width:713px;height:27px;background:#fff}
.logo{left:76px;top:6px;font-size:14px;font-weight:400;color:#555;letter-spacing:.1px}
.help-btn{left:596px;top:8px;width:39px;height:13px;border-radius:2px;background:var(--green);color:#fff;font-size:6.5px;font-weight:600;display:flex;align-items:center;justify-content:center;gap:3px}
.help-btn i{width:6px;height:6px;border-radius:50%;background:#fff;color:var(--green);font-style:normal;font-size:5px;line-height:6px;text-align:center}

/* hero */
.hero-photo{left:0;top:27px;width:713px;height:347px;background:linear-gradient(180deg,var(--hero-top) 0%,var(--hero-bottom) 100%)}
.search-card{left:77px;top:82px;width:209px;height:240px;background:#f7f7f5;border-radius:2px;box-shadow:0 1px 3px rgba(0,0,0,.25)}
.search-card label{position:absolute;left:17px;font-size:9px;line-height:11px;color:#888;font-weight:400}
.search-card .field{position:absolute;left:17px;width:174px;height:21px;background:#fff;border:1px solid #d8d8d8;border-radius:2px}
.search-btn{position:absolute;left:17px;top:188px;width:174px;height:22px;border-radius:2px;background:linear-gradient(#e9494a,var(--red-dark));color:#fff;font-size:11px;font-weight:700;font-style:italic;display:flex;align-items:center;justify-content:center;letter-spacing:.4px}
.card-mark{position:absolute;right:12px;top:18px}
.hero-banner{left:286px;top:241px}
.hero-text{left:306px;top:262px;color:#fff;font-weight:300}
.hero-text .small{font-size:14px;line-height:18px}
.hero-text .big{font-size:21px;line-height:26px}

/* content */
.section-title{left:76px;top:388px;font-size:25px;font-weight:300;color:var(--ink)}
.section-title span{color:var(--red)}
.results{left:77px;top:437px;width:400px;height:543px;background:var(--panel);border:1px solid #e6e2e2;border-radius:2px;box-shadow:0 1px 2px rgba(0,0,0,.06)}
.result{position:absolute;left:0;width:398px;height:122px}
.result.alt{background:var(--alt)}
.thumb{position:absolute;left:13px;top:7px;width:86px;height:63px;background:#fff;border:1px solid #ddd;padding:3px;box-shadow:0 1px 2px rgba(0,0,0,.1)}
.thumb div{width:100%;height:100%;background:var(--thumb)}
.result h3{position:absolute;left:108px;top:8px;font-size:10px;font-weight:400;color:var(--red)}
.result .rule{position:absolute;left:108px;top:23px;width:252px;height:1px;background:var(--line)}
.facts{position:absolute;left:108px;top:27px;font-size:6.3px;line-height:10.7px;color:#333}
.facts dt{position:absolute;left:0;font-weight:600}
.facts dd{position:absolute;left:44px;white-space:nowrap}
.facts .price{color:var(--red)}
.rating{position:absolute;left:155px;top:71px;width:87px;height:3px;background:#ddd;border-radius:2px}
.rating b{display:block;width:89%;height:100%;background:var(--green);border-radius:2px}
.rating-val{position:absolute;left:250px;top:67px;font-size:7px;color:var(--green)}
.desc{position:absolute;left:13px;top:84px;width:375px;font-size:6.3px;line-height:11px;color:#444}
.desc a{color:var(--red);text-decoration:none}
.pager-rule{position:absolute;left:13px;top:512px;width:374px;height:1px;background:var(--line)}
.pg{position:absolute;top:519px;height:12px;border:1px solid #ddd;border-radius:2px;background:#fff;font-size:6px;color:#777;display:flex;align-items:center;justify-content:center}
.pg.current{background:#eee}

/* sidebar */
.widget{left:500px;width:136px;background:#f7f6f6;border:1px solid #e2dede;border-radius:2px;box-shadow:0 1px 2px rgba(0,0,0,.06)}
.widget h4{position:absolute;left:9px;top:6px;font-size:10px;font-weight:400;color:var(--red);display:flex;align-items:center;gap:4px}
.widget .rule{position:absolute;left:8px;top:25px;width:118px;height:1px;background:var(--line)}
.widget ul{position:absolute;left:8px;top:34px;width:119px;list-style:none}
.widget li{height:13.8px;font-size:6px;color:#444;display:flex;align-items:center;justify-content:space-between;padding:0 18px 0 5px}
.widget li:nth-child(odd){background:#ececec}

/* footer */
.footer{left:0;top:1010px;width:713px;height:190px;background:var(--footer)}
.f-head{font-size:9.5px;color:#fff;font-weight:400;display:flex;align-items:center;gap:4px}
.f-rule{height:1px;background:#333}
.f-arrows{display:flex;gap:2px}
.f-arrows i{width:8px;height:8px;background:#3a3a3a;border-radius:1px;display:block}
.f-shot{top:1058px;width:84px;height:40px;border:1px solid #444}
.f-meta{font-size:6px;line-height:10.5px;color:var(--footer-text)}
.chirp-box{left:298px;top:1047px;width:150px;height:95px;background:var(--footer-box);border-radius:2px}
.chirp-box p{position:absolute;left:12px;top:8px;width:130px;font-size:6.3px;line-height:10px;color:#aaa}
.chirp-box p span{color:var(--red)}
.chirp-date{position:absolute;left:12px;top:72px}
.chirp-date span{position:absolute;left:0;top:0;width:52px;height:14px;color:#fff;font-size:6.3px;line-height:14px;padding-left:8px}
.chirp-author{position:absolute;right:14px;top:76px;font-size:7px;color:var(--blue)}
.social{left:483px;top:1056px;list-style:none}
.social li{display:flex;align-items:center;gap:9px;height:21px;font-size:6.5px;color:#ddd}
.social i{width:15px;height:15px;border-radius:2px;display:block}
.sitemap{left:573px;top:1051px;list-style:none}
.sitemap li{font-size:6.5px;line-height:11px;color:#aaa}
.sitemap li::before{content:"→ ";color:#666}
.copy{left:536px;top:1172px;font-size:6px;color:#aaa}
</style>
</head>
<body>
<div class="page">

  <header class="topbar abs">
    <div class="logo abs">Zestmora In London</div>
    <div class="help-btn abs">Help <i>?</i></div>
  </header>

  <section class="hero">
    <div class="hero-photo abs" role="img" aria-label="Panoramic food photo: a stuffed pita with falafel on a plate over a checked tablecloth"></div>

    <form class="search-card abs">
      <svg class="card-mark" width="12" height="10" viewBox="0 0 12 10"><path d="M1 3 L7 9 M4 1 L10 7" stroke="#e1393a" stroke-width="1.6"/></svg>
      <label style="top:24px">What Restaurant?</label>
      <div class="field" style="top:36px"></div>
      <label style="top:65px">What king of food?</label>
      <div class="field" style="top:77px"></div>
      <label style="top:106px">Where?</label>
      <div class="field" style="top:118px"></div>
      <label style="top:146px">Prices?</label>
      <div class="field" style="top:158px"></div>
      <div class="search-btn">Search Now</div>
    </form>

    <svg class="hero-banner abs" width="290" height="81" viewBox="0 0 290 81">
      <path d="M0 0 H256 L290 81 H0 Z" fill="#1a1a1a" fill-opacity=".92"/>
    </svg>
    <div class="hero-text abs">
      <div class="small">Find the Best</div>
      <div class="big">Restaurant In London</div>
    </div>
  </section>

  <h2 class="section-title abs">Best <span>Restaurants</span> Near You</h2>

  <main class="results abs">
    <article class="result" style="top:8px">
      <div class="thumb"><div role="img" aria-label="Restaurant sign photo"></div></div>
      <h3>Verano Restaurant</h3><div class="rule"></div>
      <dl class="facts">
        <dt style="top:0">Locations</dt><dd style="top:0">218 Harrow Lane Westbury, MD(Maryland)</dd>
        <dt style="top:10.7px">Category</dt><dd style="top:10.7px">Indian Restaurant &nbsp;(5)</dd>
        <dt style="top:21.4px">Price</dt><dd style="top:21.4px">Casual Restaurant ( <span class="price">$10- $20</span> )</dd>
        <dt style="top:32.1px">Rating</dt>
      </dl>
      <div class="rating"><b></b></div><div class="rating-val">89%</div>
      <p class="desc">Sodales ac ultrices! Modi, hendrerit. Dis eos metus pulvinar. Velit. Exercitation? Voluptatem corrupti molestiae, nostra a nisl facilisis ea, gravida placerat sociosqu rerum massa! Inventore accusantium sociis similique illum deleniti praesentium, minus. Iaculis temporibus... <a href="#">Read More...</a></p>
    </article>

    <article class="result alt" style="top:127px">
      <div class="thumb"><div role="img" aria-label="Restaurant sign photo"></div></div>
      <h3>Verano Restaurant</h3><div class="rule"></div>
      <dl class="facts">
        <dt style="top:0">Locations</dt><dd style="top:0">218 Harrow Lane Westbury, MD(Maryland)</dd>
        <dt style="top:10.7px">Category</dt><dd style="top:10.7px">Indian Restaurant &nbsp;(5)</dd>
        <dt style="top:21.4px">Price</dt><dd style="top:21.4px">Casual Restaurant ( <span class="price">$10- $20</span> )</dd>
        <dt style="top:32.1px">Rating</dt>
      </dl>
      <div class="rating"><b></b></div><div class="rating-val">89%</div>
      <p class="desc">Sodales ac ultrices! Modi, hendrerit. Dis eos metus pulvinar. Velit. Exercitation? Voluptatem corrupti molestiae, nostra a nisl facilisis ea, gravida placerat sociosqu rerum massa! Inventore accusantium sociis similique illum deleniti praesentium, minus. Iaculis temporibus... <a href="#">Read More...</a></p>
    </article>

    <article class="result" style="top:249px">
      <div class="thumb"><div role="img" aria-label="Restaurant sign photo"></div></div>
      <h3>Verano Restaurant</h3><div class="rule"></div>
      <dl class="facts">
        <dt style="top:0">Locations</dt><dd style="top:0">218 Harrow Lane Westbury, MD(Maryland)</dd>
        <dt style="top:10.7px">Category</dt><dd style="top:10.7px">Indian Restaurant &nbsp;(5)</dd>
        <dt style="top:21.4px">Price</dt><dd style="top:21.4px">Casual Restaurant ( <span class="price">$10- $20</span> )</dd>
        <dt style="top:32.1px">Rating</dt>
      </dl>
      <div class="rating"><b></b></div><div class="rating-val">89%</div>
      <p class="desc">Sodales ac ultrices! Modi, hendrerit. Dis eos metus pulvinar. Velit. Exercitation? Voluptatem corrupti molestiae, nostra a nisl facilisis ea, gravida placerat sociosqu rerum massa! Inventore accusantium sociis similique illum deleniti praesentium, minus. Iaculis temporibus... <a href="#">Read More...</a></p>
    </article>

    <article class="result alt" style="top:370px">
      <div class="thumb"><div role="img" aria-label="Restaurant sign photo"></div></div>
      <h3>Verano Restaurant</h3><div class="rule"></div>
      <dl class="facts">
        <dt style="top:0">Locations</dt><dd style="top:0">218 Harrow Lane Westbury, MD(Maryland)</dd>
        <dt style="top:10.7px">Category</dt><dd style="top:10.7px">Indian Restaurant &nbsp;(5)</dd>
        <dt style="top:21.4px">Price</dt><dd style="top:21.4px">Casual Restaurant ( <span class="price">$10- $20</span> )</dd>
        <dt style="top:32.1px">Rating</dt>
      </dl>
      <div class="rating"><b></b></div><div class="rating-val">89%</div>
      <p class="desc">Sodales ac ultrices! Modi, hendrerit. Dis eos metus pulvinar. Velit. Exercitation? Voluptatem corrupti molestiae, nostra a nisl facilisis ea, gravida placerat sociosqu rerum massa! Inventore accusantium sociis similique illum deleniti praesentium, minus. Iaculis temporibus... <a href="#">Read More...</a></p>
    </article>

    <nav class="pagination">
      <div class="pager-rule"></div>
      <div class="pg" style="left:13px;width:41px">« Prev</div>
      <div class="pg" style="left:144px;width:13px">1</div>
      <div class="pg current" style="left:162px;width:13px">2</div>
      <div class="pg" style="left:180px;width:13px">3</div>
      <div class="pg" style="left:197px;width:13px">4</div>
      <div class="pg" style="left:215px;width:13px">5</div>
      <div class="pg" style="left:340px;width:41px">Next »</div>
    </nav>
  </main>

  <aside>
    <section class="widget abs" style="top:437px;height:128px">
      <h4><svg width="8" height="7" viewBox="0 0 8 7"><rect x="0" y="2" width="8" height="5" fill="#333"/><rect x="2.5" y="0" width="3" height="2" fill="none" stroke="#333"/></svg>Categories</h4>
      <div class="rule"></div>
      <ul>
        <li><span>→ &nbsp;Italian</span><span>(4)</span></li>
        <li><span>→ &nbsp;Indian</span><span>(1)</span></li>
        <li><span>→ &nbsp;Italian</span><span>(10)</span></li>
        <li><span>→ &nbsp;Indian</span><span>(4)</span></li>
        <li><span>→ &nbsp;Italian</span><span>(6)</span></li>
        <li><span>→ &nbsp;Indian</span><span>(5)</span></li>
      </ul>
    </section>
    <section class="widget abs" style="top:570px;height:128px">
      <h4><svg width="6" height="8" viewBox="0 0 6 8"><path d="M3 8 L0.5 3.5 A2.7 2.7 0 1 1 5.5 3.5 Z" fill="#333"/><circle cx="3" cy="2.8" r="1" fill="#f7f6f6"/></svg>Locations</h4>
      <div class="rule"></div>
      <ul>
        <li><span>Restaurants In west london</span><span>(4)</span></li>
        <li><span>Restaurants In west london</span><span>(1)</span></li>
        <li><span>Restaurants In west london</span><span>(10)</span></li>
        <li><span>Restaurants In west london</span><span>(4)</span></li>
        <li><span>Restaurants In west london</span><span>(6)</span></li>
        <li><span>Restaurants In west london</span><span>(5)</span></li>
      </ul>
    </section>
  </aside>

  <footer class="footer abs"></footer>

  <div class="abs" style="left:77px;top:1030px;width:194px">
    <div style="display:flex;justify-content:space-between;align-items:center">
      <div class="f-head"><svg width="9" height="7" viewBox="0 0 9 7"><rect x=".5" y=".5" width="8" height="6" fill="none" stroke="#fff"/><rect x="2" y="2" width="2" height="2" fill="#fff"/></svg>Latest Restaurant</div>
      <div class="f-arrows"><i></i><i></i></div>
    </div>
    <div class="f-rule" style="margin-top:6px"></div>
  </div>
  <div class="f-shot abs" style="left:77px;background:linear-gradient(180deg,#e9a33a,#b4443a)" role="img" aria-label="City landmark at sunset"></div>
  <div class="f-shot abs" style="left:178px;background:linear-gradient(180deg,#a9dcec,#e9e2c4)" role="img" aria-label="Fresh drinks on a beach table"></div>
  <div class="f-meta abs" style="left:77px;top:1102px;width:95px">218 Harrow Lane Westbury, MD(Maryland)<br>Indian Restaurant &nbsp;(5)<br>Casual Restaurant ( $10- $20 )</div>
  <div class="f-meta abs" style="left:178px;top:1102px;width:95px">218 Harrow Lane Westbury, MD(Maryland)<br>Indian Restaurant &nbsp;(5)<br>Casual Restaurant ( $10- $20 )</div>

  <div class="abs" style="left:298px;top:1030px;width:150px">
    <div style="display:flex;justify-content:space-between;align-items:center">
      <div class="f-head" style="color:var(--blue)"><svg width="8" height="8" viewBox="0 0 8 8"><circle cx="4" cy="4" r="3.5" fill="#2d8fd6"/></svg>Latest Chirps</div>
      <div class="f-arrows"><i></i><i></i></div>
    </div>
  </div>
  <div class="chirp-box abs">
    <p><span>Dis eos metu@pulvinar.</span> Velit. Exercitation? Voluptatem corrupti molestiae, nostra a nisl facilisis ea, gravida placerat sociosqu rerum massa! Inventore accusantium sociis similique illum deleniti praesentium,</p>
    <div class="chirp-date">
      <svg width="60" height="14" viewBox="0 0 60 14"><path d="M0 0 H60 L54 7 L60 14 H0 Z" fill="#2d8fd6"/></svg>
      <span>25th Nov.</span>
    </div>
    <div class="chirp-author">Orla K.T.</div>
  </div>

  <div class="f-head abs" style="left:483px;top:1030px">Follow Us On</div>
  <ul class="social abs">
    <li><i style="background:#3b5998"></i>Friendlane</li>
    <li><i style="background:#2f74a8"></i>Chirpline</li>
    <li><i style="background:#c4302b"></i>Reelcast</li>
    <li><i style="background:#46a33e"></i>Mailer</li>
  </ul>

  <div class="f-head abs" style="left:573px;top:1030px"><svg width="8" height="7" viewBox="0 0 8 7"><rect x="3" y="0" width="2" height="2" fill="#fff"/><rect x="0" y="5" width="2" height="2" fill="#fff"/><rect x="6" y="5" width="2" height="2" fill="#fff"/><path d="M4 2 V3.5 M1 5 V3.5 H7 V5" stroke="#fff" stroke-width=".8" fill="none"/></svg>Site Map</div>
  <div class="f-rule abs" style="left:573px;top:1045px;width:62px"></div>
  <ul class="sitemap abs">
    <li>Home</li><li>About Us</li><li>Help</li><li>Locations</li><li>Restaurants</li><li>Prices</li><li>Categories</li>
  </ul>

  <div class="f-rule abs" style="left:77px;top:1165px;width:558px"></div>
  <div class="copy abs">©copyrights 2013 all rights reserved.</div>

</div>
</body>
</html>
```